business card design

i would like business cards designed. My business provides trade qualified personnel to the mining industry to work on heavy mobile equipment.
please put a excavator(digger) in the background in one design and have one design without so i can compare the difference.
also add info:
my logo(attached) and "mobile equipment repair and maintenance"
name: Derek Holloway
address: 57 Tarrowby RD Ashcombe Perth WA.
mobile: 0438120957
email: derek@ironvalemx.com

```html
<!DOCTYPE html>
<html lang="en">
<head>
<meta charset="utf-8">
<title>Ironvale Maintenance Services – Business Cards</title>
<link rel="stylesheet" href="https://fonts.googleapis.com/css2?family=Poppins:wght@400;500;600;700;800&display=swap">
<style>
  :root {
    --navy: #13285c;
    --blue: #3b6bc6;
    --white: #ffffff;
    --ink: #1a1f2e;
    --stage: #e7e8eb;
    --machine-yellow: #f2a81f;
    --machine-dark: #3a3d42;
  }
  * { box-sizing: border-box; margin: 0; padding: 0; }
  html, body { width: 1200px; height: 780px; overflow: hidden; }
  body {
    background: var(--stage);
    font-family: "Poppins", sans-serif;
    color: var(--ink);
    position: relative;
  }
  .card {
    position: absolute;
    width: 540px;
    height: 309px;
    background: var(--white);
    box-shadow: 0 10px 28px rgba(0,0,0,.18);
    overflow: hidden;
  }
  .card--front { left: 40px; top: 236px; }
  .card--back  { left: 620px; top: 236px; }

  .machine-photo {
    position: absolute;
    background: radial-gradient(ellipse at 60% 40%, var(--machine-yellow) 0%, #e9b04a 38%, #8b8d91 70%, var(--machine-dark) 100%);
    border-radius: 4px;
    opacity: .92;
  }
  .card--front .machine-photo { left: 18px; top: 14px; width: 228px; height: 186px; }
  .card--back .machine-photo { right: 0; top: 118px; width: 190px; height: 191px; border-radius: 4px 0 0 0; }

  .brand { position: absolute; }
  .brand__name {
    display: block;
    font-weight: 800;
    color: var(--navy);
    letter-spacing: 2px;
    line-height: 1;
  }
  .brand__sub {
    display: block;
    font-weight: 500;
    color: var(--blue);
    letter-spacing: 1px;
    white-space: nowrap;
  }
  .card--front .brand { left: 262px; top: 102px; }
  .card--front .brand__name { font-size: 44px; }
  .card--front .brand__sub { font-size: 8.6px; margin-top: 4px; }
  .card--back .brand { left: 40px; top: 30px; }
  .card--back .brand__name { font-size: 46px; }
  .card--back .brand__sub { font-size: 9px; margin-top: 4px; }

  .tagline-band { position: absolute; left: 0; width: 100%; height: 60px; }
  .card--front .tagline-band { top: 208px; }
  .card--back .tagline-band { top: 232px; }
  .tagline {
    position: absolute;
    color: var(--white);
    font-size: 11px;
    letter-spacing: .3px;
    white-space: nowrap;
  }
  .card--front .tagline { left: 18px; top: 210px; }
  .card--back .tagline { left: 24px; top: 234px; }

  .contact { position: absolute; left: 40px; top: 118px; font-size: 12px; line-height: 1.45; }
  .contact__name { font-size: 14px; margin-bottom: 4px; letter-spacing: .3px; }
  .contact__first { color: var(--blue); font-weight: 600; }
  .contact__last { color: var(--navy); font-weight: 700; }
  .contact__line { display: flex; align-items: center; gap: 6px; }
  .contact__icon { width: 11px; height: 11px; flex: none; }
</style>
</head>
<body>

  <section class="card card--front" aria-label="Business card front">
    <div class="machine-photo" role="img" aria-label="Photograph of a yellow tracked excavator with its arm raised"></div>
    <div class="brand">
      <span class="brand__name">IRONVALE</span>
      <span class="brand__sub">MAINTENANCE SERVICES PTY LTD</span>
    </div>
    <svg class="tagline-band" viewBox="0 0 540 60" aria-hidden="true">
      <polygon points="0,0 420,0 410,20 0,20" fill="var(--navy)"/>
      <polygon points="418,38 452,38 444,56 410,56" fill="var(--blue)"/>
      <polygon points="460,38 494,38 486,56 452,56" fill="var(--blue)"/>
    </svg>
    <p class="tagline">mobile equipment repair and maintenance</p>
  </section>

  <section class="card card--back" aria-label="Business card back">
    <div class="brand">
      <span class="brand__name">IRONVALE</span>
      <span class="brand__sub">MAINTENANCE SERVICES PTY LTD</span>
    </div>
    <div class="contact">
      <p class="contact__name"><span class="contact__first">DEREK</span> <span class="contact__last">HOLLOWAY</span></p>
      <p>57 Tarrowby RD</p>
      <p>Ashcombe Perth WA.</p>
      <p class="contact__line">
        <svg class="contact__icon" viewBox="0 0 12 12" aria-hidden="true"><path d="M3 1 L5 3.5 L4 5 Q5.5 7 7 8 L8.5 7 L11 9 L9.5 11 Q4 10 1 2.5 Z" fill="var(--blue)"/></svg>
        0438120957
      </p>
      <p class="contact__line">
        <svg class="contact__icon" viewBox="0 0 12 12" aria-hidden="true"><rect x="0.5" y="2.5" width="11" height="7" fill="none" stroke="var(--blue)" stroke-width="1.2"/><path d="M0.5 2.5 L6 6.5 L11.5 2.5" fill="none" stroke="var(--blue)" stroke-width="1.2"/></svg>
        derek@ironvalemx.com
      </p>
    </div>
    <svg class="tagline-band" viewBox="0 0 540 60" aria-hidden="true">
      <polygon points="0,0 342,0 334,20 0,20" fill="var(--navy)"/>
      <polygon points="272,40 302,40 294,58 264,58" fill="var(--blue)"/>
      <polygon points="310,40 340,40 332,58 302,58" fill="var(--blue)"/>
    </svg>
    <p class="tagline">mobile equipment repair and maintenance</p>
    <div class="machine-photo" role="img" aria-label="Photograph of a yellow excavator bucket and arm with tracks, cropped at the card edge"></div>
  </section>

</body>
</html>
```